Modern, Sleek Business Card Design for Corvane Systems

Please create a modern business card, preferably all black with white logo and writing for Corvane Systems, a defense and aerospace company.

Contact Information for Business Card

symbol on one side and name, title, contact info on the other side.

```html
<!DOCTYPE html>
<html lang="en">
<head>
<meta charset="UTF-8">
<title>Corvane Systems — Business Card</title>
<link rel="stylesheet" href="https://fonts.googleapis.com/css2?family=Montserrat:wght@300;400;600;800&display=swap">
<style>
  :root {
    --backdrop: #d9d9d6;
    --card: #ffffff;
    --ink: #111111;
    --muted: #2a2a2a;
    --shadow: rgba(0, 0, 0, 0.18);
  }
  * { margin: 0; padding: 0; box-sizing: border-box; }
  html, body {
    width: 1200px;
    height: 801px;
    overflow: hidden;
    background: var(--backdrop);
    font-family: "Montserrat", sans-serif;
    color: var(--ink);
  }
  .stage {
    position: relative;
    width: 1200px;
    height: 801px;
  }
  .card {
    position: absolute;
    top: 245px;
    width: 540px;
    height: 310px;
    background: var(--card);
    box-shadow: 0 8px 24px var(--shadow);
  }
  .card--back { left: 40px; }
  .card--front { left: 620px; }

  /* back side */
  .card--back .brand-block {
    position: absolute;
    left: 0;
    top: 0;
    width: 250px;
    height: 100%;
    display: flex;
    align-items: center;
    justify-content: center;
  }
  .brand-name--small {
    font-weight: 600;
    font-size: 19px;
    letter-spacing: 2px;
    text-transform: uppercase;
  }
  .divider {
    position: absolute;
    left: 250px;
    top: 78px;
    width: 1.5px;
    height: 170px;
    background: var(--ink);
  }
  .details {
    position: absolute;
    left: 280px;
    top: 62px;
    width: 240px;
  }
  .person-name {
    font-weight: 800;
    font-size: 22px;
    letter-spacing: 0.5px;
    text-transform: uppercase;
    line-height: 1.1;
  }
  .person-title {
    font-weight: 300;
    font-size: 13.5px;
    color: var(--muted);
    margin-top: 3px;
  }
  .address {
    font-weight: 300;
    font-size: 13.5px;
    color: var(--muted);
    margin-top: 16px;
    line-height: 1.45;
  }
  .contact-list {
    list-style: none;
    margin-top: 12px;
  }
  .contact-item {
    display: flex;
    align-items: center;
    gap: 8px;
    font-weight: 300;
    font-size: 13.5px;
    color: var(--muted);
    line-height: 1.55;
  }
  .contact-icon { width: 11px; height: 11px; flex: none; }

  /* front side */
  .card--front {
    display: flex;
    align-items: center;
    justify-content: center;
  }
  .brand-name--large {
    font-weight: 600;
    font-size: 38px;
    letter-spacing: 4px;
    text-transform: uppercase;
  }
</style>
</head>
<body>
<main class="stage">
  <section class="card card--back" aria-label="Card back with contact details">
    <div class="brand-block">
      <span class="brand-name--small">Corvane Systems</span>
    </div>
    <div class="divider"></div>
    <div class="details">
      <h1 class="person-name">Elias Marrow</h1>
      <p class="person-title">Managing Director</p>
      <p class="address">Your address, City<br>State, Zip 1234</p>
      <ul class="contact-list">
        <li class="contact-item">
          <svg class="contact-icon" viewBox="0 0 12 12" aria-hidden="true"><path d="M2 1h2.5l1 3-1.5 1a6 6 0 0 0 3 3l1-1.5 3 1V11a1 1 0 0 1-1 1A10 10 0 0 1 0 2a1 1 0 0 1 2-1z" fill="#111"/></svg>
          555 014 2290
        </li>
        <li class="contact-item">
          <svg class="contact-icon" viewBox="0 0 12 12" aria-hidden="true"><rect x="0" y="2" width="12" height="8" fill="#111"/><path d="M0 2l6 4.5L12 2" stroke="#fff" stroke-width="1" fill="none"/></svg>
          info@corvanemail.com
        </li>
        <li class="contact-item">
          <svg class="contact-icon" viewBox="0 0 12 12" aria-hidden="true"><circle cx="6" cy="6" r="5.5" fill="#111"/><path d="M0.5 6h11M6 0.5c-3 3-3 8 0 11M6 0.5c3 3 3 8 0 11" stroke="#fff" stroke-width="0.7" fill="none"/></svg>
          www.corvanesys.com
        </li>
      </ul>
    </div>
  </section>

  <section class="card card--front" aria-label="Card front">
    <span class="brand-name--large">Corvane Systems</span>
  </section>
</main>
</body>
</html>
```